Simple and clean

We need a business card design for a new company called Estate Lantern. It is a search engine to find current properties for sale or rent in New Zealand market.
We have already a colour scheme that we would like people to use.
Light brown: #D4CCB0
Light green: #D6E4D4
Green: #669966
Black/White
It is OK to divert from this colour scheme slightly as long as there is a green component to the business card.
Final design should be clean, simple and should communicate the nature of the business.
Target Market(s)
- First home buyers
- Real estate agents
- People seeking rentals
Industry/Entity Type
Business
Requirements
Must have
- Use those or similar colours.
Light brown: #D4CCB0
Light green: #D6E4D4
Green: #669966
Black/White

```html
<!DOCTYPE html>
<html lang="en">
<head>
<meta charset="utf-8">
<title>Estate Lantern – Business Card</title>
<link rel="stylesheet" href="https://fonts.googleapis.com/css2?family=Source+Sans+3:ital,wght@0,400;0,700;1,400&display=swap">
<style>
  :root {
    --card-black: #000000;
    --frame-grey: #b5b5b5;
    --sage: #d2d9ad;
    --brand-green: #5bbf45;
    --ink: #111111;
    --web-grey: #a9a9a9;
    --badge-fill: #e6e6e6;
    --badge-ring: #ffffff;
  }
  html, body {
    margin: 0;
    padding: 0;
    width: 1200px;
    height: 702px;
    overflow: hidden;
    background: #ffffff;
  }
  .card {
    position: relative;
    width: 1200px;
    height: 702px;
    background: var(--card-black);
    box-sizing: border-box;
    border: 2px solid var(--frame-grey);
    overflow: hidden;
    font-family: "Source Sans 3", "Myriad Pro", Arial, sans-serif;
  }
  .sage-curve {
    position: absolute;
    inset: 0;
    width: 100%;
    height: 100%;
  }
  .brand {
    position: absolute;
    left: 58px;
    top: 56px;
    display: flex;
    align-items: center;
    gap: 24px;
  }
  .brand-badge {
    width: 156px;
    height: 156px;
    border-radius: 50%;
    background: var(--badge-fill);
    border: 6px solid var(--badge-ring);
    box-sizing: border-box;
  }
  .brand-name {
    margin: 0 0 40px 0;
    font-size: 66px;
    font-weight: 400;
    color: var(--brand-green);
    letter-spacing: -0.5px;
    line-height: 1;
  }
  .contact {
    position: absolute;
    right: 71px;
    top: 212px;
    text-align: right;
    color: var(--ink);
  }
  .contact-name {
    margin: 0;
    font-size: 34px;
    font-weight: 700;
    line-height: 1.2;
  }
  .contact-role {
    margin: 2px 0 0;
    font-size: 29px;
    font-style: italic;
    line-height: 1.2;
  }
  .contact-details {
    margin: 46px 0 0;
    font-size: 28px;
    line-height: 45px;
  }
  .website {
    position: absolute;
    left: 67px;
    bottom: 52px;
    margin: 0;
    font-size: 50px;
    color: var(--web-grey);
    line-height: 1;
  }
</style>
</head>
<body>
  <div class="card">
    <svg class="sage-curve" viewBox="0 0 1200 702" aria-hidden="true">
      <path d="M1200 0 L1162 0 C840 40 598 190 598 345 C598 520 850 680 1132 702 L1200 702 Z" fill="var(--sage)"/>
    </svg>

    <div class="brand">
      <div class="brand-badge"></div>
      <p class="brand-name">Estate Lantern</p>
    </div>

    <div class="contact">
      <p class="contact-name">Aaron Whitley</p>
      <p class="contact-role">Director</p>
      <p class="contact-details">
        Mobile: 04x-xxx-xxxx<br>
        Email: a.whitley@estatelantern.co.nz
      </p>
    </div>

    <p class="website">www.estatelantern.co.nz</p>
  </div>
</body>
</html>
```